Tunnel

a graphic meme to be sent to my clients, consisting of a long angular dark tunnel with a bright light at one end; located within the bright light at the end of the tunnel is the number 2021
the illuminated (shiny silver?) 3 dimensional font message running along the left wall of the tunnel is: BE SAFE.!
the smaller font message underneath the graphic is: Best Wishes For a Healthy New Year
Lem Dortvan Mediator (also to be included nearby is a small semi-circle logo of my corporate logo).

Font styles to use
Sans Serif
Other font styles liked:
• 3 dimensional bold lettering for BE SAFE

```html
<!DOCTYPE html>
<html lang="en">
<head>
<meta charset="utf-8">
<title>Be Safe – New Year Greeting</title>
<link rel="stylesheet" href="https://fonts.googleapis.com/css2?family=Anton&family=Cinzel+Decorative:wght@400&family=Lora:wght@400&family=Roboto+Slab:wght@300;400&display=swap">
<style>
  :root {
    --tunnel-dark: #0b0b0b;
    --tunnel-mid: #2b2a28;
    --tunnel-light: #eef0ed;
    --accent-gold: #f1b515;
    --paper: #ffffff;
    --headline-face: #e8e8e8;
    --headline-side: #8a8a8a;
    --year-ink: rgba(70, 72, 70, 0.55);
    --ink-soft: #555555;
    --ink-muted: #6a6a6a;
    --rule: #cfcfcf;
    --brand-navy: #1c1f5e;
  }
  html, body {
    margin: 0;
    padding: 0;
    overflow: hidden;
  }
  body {
    width: 892px;
    height: 1200px;
    background: var(--paper);
  }
  .card {
    position: relative;
    width: 892px;
    height: 1200px;
    overflow: hidden;
    background: var(--paper);
  }
  .hero {
    position: absolute;
    left: 0;
    top: 0;
  }
  .year {
    font-family: "Anton", sans-serif;
    font-size: 64px;
    letter-spacing: 3px;
    fill: var(--year-ink);
  }
  .headline {
    position: absolute;
    left: 80px;
    top: 452px;
    margin: 0;
    font-family: "Anton", sans-serif;
    font-weight: 400;
    font-size: 240px;
    line-height: 1;
    letter-spacing: 4px;
    color: var(--headline-face);
    transform-origin: left center;
    transform: perspective(700px) rotateY(26deg) scaleX(1.02);
    text-shadow:
      2px 2px 0 #bdbdbd,
      4px 3px 0 #a9a9a9,
      6px 4px 0 #9a9a9a,
      8px 5px 0 var(--headline-side),
      10px 6px 0 #777,
      12px 8px 10px rgba(0,0,0,0.6);
    white-space: nowrap;
  }
  .greeting {
    position: absolute;
    left: 0;
    width: 892px;
    top: 752px;
    margin: 0;
    text-align: center;
    font-family: "Cinzel Decorative", serif;
    font-weight: 400;
    font-size: 50px;
    line-height: 62px;
    letter-spacing: 1px;
    color: var(--paper);
  }
  .greeting-rule {
    position: absolute;
    left: 293px;
    top: 898px;
    width: 262px;
    height: 2px;
    background: var(--rule);
  }
  .portrait {
    position: absolute;
    left: 82px;
    top: 1028px;
    width: 123px;
    height: 144px;
    background: linear-gradient(180deg, #9ea5ab 0%, #7d858c 55%, #2a2c34 100%);
  }
  .contact {
    position: absolute;
    left: 230px;
    top: 1044px;
  }
  .contact-name {
    margin: 0;
    font-family: "Lora", serif;
    font-size: 29px;
    letter-spacing: 3px;
    color: var(--ink-soft);
    line-height: 36px;
  }
  .contact-role {
    margin: 0 0 20px;
    font-family: "Roboto Slab", serif;
    font-weight: 300;
    font-size: 15px;
    letter-spacing: 1px;
    color: var(--accent-gold);
  }
  .contact-line {
    margin: 0;
    font-family: "Roboto Slab", serif;
    font-weight: 300;
    font-size: 16px;
    letter-spacing: 1.5px;
    line-height: 24px;
    color: var(--ink-muted);
  }
  .brand {
    position: absolute;
    left: 604px;
    top: 1082px;
    display: flex;
    align-items: center;
    gap: 12px;
  }
  .brand-dot {
    width: 34px;
    height: 34px;
    border-radius: 50%;
    background: var(--brand-navy);
  }
  .brand-name {
    font-family: "Lora", serif;
    font-size: 22px;
    letter-spacing: 2px;
    color: var(--brand-navy);
  }
</style>
</head>
<body>
<main class="card">
  <svg class="hero" width="892" height="1000" viewBox="0 0 892 1000">
    <defs>
      <radialGradient id="tunnelGlow" cx="680" cy="470" r="620" gradientUnits="userSpaceOnUse">
        <stop offset="0" stop-color="var(--tunnel-light)" />
        <stop offset="0.12" stop-color="#bfc3c0" />
        <stop offset="0.35" stop-color="var(--tunnel-mid)" />
        <stop offset="0.75" stop-color="var(--tunnel-dark)" />
        <stop offset="1" stop-color="#050505" />
      </radialGradient>
    </defs>
    <polygon class="tunnel-photo" role="img" aria-label="Photograph of a long dark stone tunnel with bright light at the far end"
      points="0,0 892,0 892,930 0,978" fill="url(#tunnelGlow)" />
    <text class="year" x="680" y="494" text-anchor="middle">2021</text>
    <polygon class="accent-band" points="0,976 892,928 892,940 0,988" fill="var(--accent-gold)" />
  </svg>

  <h1 class="headline">BE SAFE!</h1>

  <p class="greeting">Best Wishes for a<br>Healthy New Year!</p>
  <div class="greeting-rule"></div>

  <div class="portrait" role="img" aria-label="Portrait photo of the mediator"></div>

  <section class="contact">
    <p class="contact-name">Lem Dortvan</p>
    <p class="contact-role">Mediator</p>
    <p class="contact-line">ldortvan@kestrel-adr.com</p>
    <p class="contact-line">Phone: (954) 555-0172</p>
  </section>

  <div class="brand">
    <span class="brand-dot"></span>
    <span class="brand-name">Kestrel Adair</span>
  </div>
</main>
</body>
</html>
```